Home Remodeler Needs a Website!

Single page (plus contact form) website for small home remodeling company. He's got a few pictures he'd like on the site and needs some basic text. He likes clean, simple designs and is "more traditional" in his stylistic preferences. Most of his business comes from word-of-mouth advertising and so the site is just something he needs for people to feel more comfortable with his business.

Target Market(s)

People who want to remodel their homes

Coding

Coded - Design and coding required

Number of Pages Required

2 page

Requirements
Must have
• Main page to include some or all of the attached images, contact page. Neutral colors. Old domain: brindlecoveabodes.com New domain: qm-holdings.com You can pull text from the old site or update it.
Should not have
• No loud colors/loud visual elements

```html
<!DOCTYPE html>
<html lang="en">
<head>
<meta charset="utf-8">
<title>Brindle Cove Abodes</title>
<link href="https://fonts.googleapis.com/css2?family=Montserrat:wght@300;500;700&family=Roboto:wght@400;500&family=Lato:wght@400;700&display=swap" rel="stylesheet">
<style>
:root{
  --ink:#111111;
  --panel:#2e2e2e;
  --panel-deep:#262626;
  --white:#ffffff;
  --field-bg:#f4f4f4;
  --field-line:#c9c9c9;
  --muted:#8a8a8a;
  --shadow-grey:#d9d9d9;
  --shadow-mid:#a9a9a9;
  --footer-bg:#eeeeee;
  --accent:#ee7a1e;
  --accent-deep:#e0661a;
}
*{box-sizing:border-box;margin:0;padding:0}
html,body{width:1200px;height:3673px;overflow:hidden;background:var(--white)}
body{position:relative;font-family:'Lato',sans-serif;color:var(--ink)}
.abs{position:absolute}
.photo{position:absolute}

/* hero */
.hero{left:0;top:0;width:1200px;height:782px;background:linear-gradient(160deg,#3d4a5a 0%,#5a4636 45%,#2b2119 100%)}
.topbar{left:0;top:0;width:1200px;height:90px;background:rgba(30,30,30,.55)}
.brand{left:66px;top:28px;font-family:'Roboto',sans-serif;font-size:27px;font-weight:500;color:var(--white)}
.nav a{position:absolute;top:38px;font-family:'Montserrat',sans-serif;font-size:14px;color:var(--white);text-decoration:none}
.social-top span{position:absolute;top:33px;width:27px;height:27px;border-radius:50%;background:var(--white)}
.hero-line1{left:0;width:1200px;top:290px;text-align:center;font-family:'Montserrat',sans-serif;font-weight:300;font-size:56px;color:var(--white);letter-spacing:1px}
.hero-line2{left:0;width:1200px;top:355px;text-align:center;font-family:'Montserrat',sans-serif;font-weight:700;font-size:60px;color:var(--white)}
.btn-pill{position:absolute;display:flex;align-items:center;justify-content:center;border-radius:30px;font-family:'Montserrat',sans-serif;font-weight:500;text-transform:uppercase}
.hero-btn{left:504px;top:443px;width:201px;height:50px;background:var(--white);color:var(--ink);font-size:14px}
.scroll{left:0;width:1200px;top:688px;text-align:center;font-family:'Montserrat',sans-serif;font-size:14px;letter-spacing:3px;color:var(--white)}

/* headings */
.sec-title{position:absolute;left:0;width:1200px;text-align:center;font-family:'Roboto',sans-serif;font-size:32px;font-weight:500;line-height:34px;color:var(--ink)}
.rule{position:absolute;height:3px;width:42px;background:var(--ink)}
.rule.light{background:var(--white)}

/* service tiles */
.tile-label{position:absolute;font-family:'Roboto',sans-serif;font-weight:500;font-size:22px;line-height:26px;color:var(--white)}
.outline-btn{left:483px;top:1532px;width:234px;height:58px;border:2px solid var(--ink);font-size:14px;letter-spacing:1px;color:var(--ink)}

/* about */
.about-box{left:58px;top:1758px;width:550px;height:441px;background:var(--panel)}
.about-box h2{position:absolute;left:68px;top:60px;font-family:'Roboto',sans-serif;font-weight:500;font-size:30px;color:var(--white)}
.about-box p{position:absolute;left:68px;top:128px;width:420px;font-size:13.5px;line-height:25px;color:var(--white)}
.about-btn{left:65px;top:322px;width:147px;height:45px;background:var(--white);color:var(--ink);font-size:13px;letter-spacing:1px}

/* booking */
.book-frame{left:663px;top:2515px;width:420px;height:321px;border:3px solid rgba(255,255,255,.85)}
.book-box{left:674px;top:2527px;width:399px;height:299px;background:var(--panel-deep)}
.book-box h2{position:absolute;left:54px;top:44px;font-family:'Roboto',sans-serif;font-weight:500;font-size:29px;line-height:36px;color:var(--white)}
.book-box p{position:absolute;left:54px;top:156px;width:320px;font-size:13.5px;line-height:22px;color:#dddddd}
.book-btn{left:52px;top:202px;width:142px;height:42px;border:2px solid var(--white);color:var(--white);font-size:12px;letter-spacing:1px}

/* contact */
.field{position:absolute;background:var(--field-bg);border:1px solid var(--field-line);font-size:13px;color:#777777;padding:14px 0 0 22px}
.send{left:516px;top:3363px;width:158px;height:43px;background:linear-gradient(180deg,var(--accent),var(--accent-deep));color:var(--white);font-size:15px;letter-spacing:1px}

/* footer */
.footer{left:0;top:3469px;width:1200px;height:204px;background:var(--footer-bg)}
.foot-nav a{position:absolute;top:42px;font-family:'Montserrat',sans-serif;font-size:15px;color:var(--ink);text-decoration:none}
.copy{left:0;width:1200px;top:80px;text-align:center;font-size:13px;color:var(--muted)}
.foot-social span{position:absolute;top:117px;width:35px;height:35px;border-radius:50%;background:var(--ink)}
</style>
</head>
<body>

<!-- hero -->
<div class="photo hero abs" role="img" aria-label="Renovated kitchen with stainless refrigerator, farmhouse sink and dark wood cabinets"></div>
<div class="abs topbar"></div>
<div class="abs brand">Brindle Cove Abodes</div>
<nav class="nav">
  <a style="left:415px">HOME</a>
  <a style="left:533px">SERVICES</a>
  <a style="left:669px">ABOUT US</a>
  <a style="left:813px">CONTACT US</a>
</nav>
<div class="social-top" aria-label="Social links">
  <span style="left:980px"></span><span style="left:1023px"></span><span style="left:1064px"></span>
</div>
<svg class="abs" style="left:42px;top:333px" width="32" height="56" viewBox="0 0 32 56"><polyline points="28,2 4,28 28,54" fill="none" stroke="#fff" stroke-width="3"/></svg>
<svg class="abs" style="left:1126px;top:333px" width="32" height="56" viewBox="0 0 32 56"><polyline points="4,2 28,28 4,54" fill="none" stroke="#fff" stroke-width="3"/></svg>
<div class="abs hero-line1">YOUR DREAM</div>
<div class="abs hero-line2">LUXURY RENOVATION</div>
<div class="btn-pill hero-btn">View Portfolio</div>
<div class="abs scroll">SCROLL</div>
<svg class="abs" style="left:585px;top:716px" width="22" height="12" viewBox="0 0 22 12"><polyline points="1,1 11,10 21,1" fill="none" stroke="#fff" stroke-width="2"/></svg>

<!-- services -->
<div class="sec-title" style="top:833px">COMMERCIAL &amp; RESIDENTIAL<br>CONTRACTING</div>
<div class="rule" style="left:583px;top:905px"></div>

<div class="photo" style="left:60px;top:945px;width:544px;height:544px;background:linear-gradient(170deg,#a9bccb 0%,#8d9aa4 50%,#5e5448 100%)" role="img" aria-label="Bathroom with soaking tub, mosaic tile band and leaded glass window"></div>
<div class="tile-label" style="left:91px;top:1400px">PRE CONSTRUCTION<br>CONSULTATION</div>
<div class="rule light" style="left:94px;top:1458px"></div>

<div class="photo" style="left:614px;top:945px;width:543px;height:268px;background:linear-gradient(160deg,#4a2c2c 0%,#6b4a32 45%,#1e1a18 100%)" role="img" aria-label="Kitchen with wood cabinetry, stone backsplash and lit wine display"></div>
<div class="tile-label" style="left:640px;top:1126px">PORCHES AND DECKS<br>HISTORIC RENOVATIONS</div>
<div class="rule light" style="left:641px;top:1185px"></div>

<div class="photo" style="left:616px;top:1221px;width:544px;height:268px;background:linear-gradient(170deg,#9a9c95 0%,#7e6a55 55%,#4a3524 100%)" role="img" aria-label="Open-plan new build with polished wood floor, kitchen bar and french doors"></div>
<div class="tile-label" style="left:638px;top:1428px">NEW CONSTRUCTION</div>
<div class="rule light" style="left:639px;top:1459px"></div>

<div class="btn-pill outline-btn">View More Services</div>

<!-- about -->
<div class="abs" style="left:281px;top:1682px;width:878px;height:634px;background:var(--shadow-grey)"></div>
<div class="abs" style="left:313px;top:1700px;width:887px;height:594px;background:var(--shadow-mid)"></div>
<div class="photo" style="left:326px;top:1663px;width:874px;height:610px;background:linear-gradient(175deg,#d9d2c6 0%,#8f7a62 40%,#d8d8d8 80%,#b3aca4 100%)" role="img" aria-label="Modern lobby with sculpted white ceiling, curved reception desk and marble floor"></div>
<div class="abs about-box">
  <h2>BRINDLE COVE ABODES</h2>
  <div class="rule light" style="left:68px;top:105px"></div>
  <p>When you want affordable, quality home construction services; think of us to do the job.Since 1981 Walter Greene has built and remodeled over 400 homes and businesses. Let us be your contractor for the next project you start. when quality, value and personal attention to detail are important With over 20 years experience in residential and commercial construction, you can trust your project to Brindle Cove Abodes.</p>
  <div class="btn-pill about-btn">Read More</div>
</div>

<!-- booking -->
<div class="photo" style="left:0;top:2401px;width:1200px;height:566px;background:linear-gradient(180deg,#e6e4e1 0%,#b9b2a8 45%,#6b5642 80%,#4a3a2c 100%)" role="img" aria-label="Hotel-style bedroom with upholstered bed, table lamps and wide plank wood floor"></div>
<div class="abs book-frame"></div>
<div class="abs book-box">
  <h2>BOOK YOUR HOME<br>RENOVATION</h2>
  <div class="rule light" style="left:54px;top:127px"></div>
  <p>Curabitur vel dolor ultrices ipsum dictum tristique Praesent vitae lacus Ut velit enim vestib</p>
  <div class="btn-pill book-btn">Book Now</div>
</div>

<!-- contact -->
<div class="sec-title" style="top:3033px;font-size:33px"><span style="font-weight:500">CONTACT</span> <span style="font-weight:400">FORM</span></div>
<div class="rule" style="left:584px;top:3073px"></div>
<div class="field" style="left:201px;top:3109px;width:402px;height:49px">First Name*</div>
<div class="field" style="left:614px;top:3109px;width:401px;height:49px">Last Name*</div>
<div class="field" style="left:201px;top:3168px;width:402px;height:48px">Email address*</div>
<div class="field" style="left:614px;top:3168px;width:401px;height:48px">Phone*</div>
<div class="field" style="left:202px;top:3229px;width:817px;height:107px">Message</div>
<div class="btn-pill send">SEND</div>

<!-- footer -->
<footer class="abs footer">
  <nav class="foot-nav">
    <a style="left:344px">HOME</a>
    <a style="left:473px">PORTFOLIO</a>
    <a style="left:643px">ABOUT US</a>
    <a style="left:803px">BOOKING</a>
  </nav>
  <div class="abs copy">© 2020 Larkspur Studio &nbsp;|&nbsp; Legal &nbsp;|&nbsp; Term of Use</div>
  <div class="foot-social" aria-label="Social links">
    <span style="left:549px"></span><span style="left:595px"></span><span style="left:642px"></span>
  </div>
</footer>

</body>
</html>
```